WordPress webdesign with coding for our company BLOOM The Answer

BLOOM The Answer is a payrolling company such as Marnex Wagework (one of our competitor https://www.marnex-wagework.ch/fr/). We need to set up our website in both languages (Fr and Eng). Our logo is enclosed.
we would like something simple explaining what is payrolling in Graph and wording, who we are and a contact page. you can also take some example if needed from our mother company BLOOM The Horizon (www.bloomthehorizon.ch) or our sister company (www.bloomyourstride.ch). we would like to keep the color panel of our logo (ref. Black = PANTONE P Process Black C
Pink = PANTONE P Process Magenta C
Grey = PANTONE 430 C) as the driver of the website.

```html
<!DOCTYPE html>
<html lang="en">
<head>
<meta charset="utf-8">
<title>BLOOM The Answer — Payrolling</title>
<link href="https://fonts.googleapis.com/css2?family=Lato:wght@300;400;700;900&display=swap" rel="stylesheet">
<style>
:root{
  --pink:#E5007E;
  --pink-soft:#F7C6DF;
  --pink-wash:#FDEEF6;
  --black:#0B0B0B;
  --grey:#7C878E;
  --text:#333;
  --white:#fff;
}
*{box-sizing:border-box;margin:0;padding:0}
html,body{width:1200px;height:4662px;overflow:hidden}
body{position:relative;background:var(--white);font-family:'Lato',sans-serif;color:var(--text)}
.abs{position:absolute}
.brand{font-weight:900;font-size:24px;letter-spacing:.5px;color:var(--black);display:flex;align-items:center;gap:10px;white-space:nowrap}
.brand .dot{width:12px;height:12px;border-radius:50%;background:var(--pink)}
.nav{top:32px;left:362px;display:flex;gap:46px;font-size:14px;color:#222;align-items:center;white-space:nowrap}
.nav .active{color:var(--pink)}
.btn{display:inline-block;background:var(--pink);color:#fff;font-weight:700;font-size:15px;padding:15px 18px;text-transform:uppercase;white-space:nowrap}
.nav .btn{padding:14px 18px;font-size:14px}
.hero-title{top:190px;left:108px;font-size:54px;font-weight:700;line-height:60px;color:var(--black);text-transform:uppercase}
.hero-text{top:314px;left:110px;width:514px;font-size:16px;line-height:28px;text-align:justify;color:#222}
.hero-btn{top:420px;left:110px}
.section-title{left:0;width:1200px;text-align:center;font-size:40px;font-weight:300;color:var(--black);text-transform:uppercase;line-height:56px}
.section-title b{font-weight:700}
.rule{left:560px;width:80px;height:5px;background:var(--pink)}
.rule::before{content:"";position:absolute;left:-60px;right:-60px;top:2px;height:1px;background:#ddd;z-index:-1}
.service{width:300px;text-align:center}
.service .ic{width:88px;height:88px;border-radius:50%;background:var(--pink);margin:0 auto 12px}
.service h3{font-size:22px;color:var(--black);margin-bottom:8px;font-weight:400}
.service p{font-size:13px;line-height:23px;color:#555}
.value{width:300px;height:362px;top:1412px;filter:drop-shadow(0 0 18px rgba(229,0,126,.16))}
.value .shape{position:absolute;inset:0;background:#fff;clip-path:polygon(0 0,88% 0,100% 50%,88% 100%,0 100%,12% 50%)}
.value .inner{position:absolute;left:68px;right:68px;top:58px;text-align:center}
.value h3{font-size:21px;font-weight:400;color:var(--black);margin:16px 0 12px;white-space:nowrap}
.value p{font-size:13px;line-height:23px;color:#444}
.value .go{position:absolute;left:50%;margin-left:-18px;top:342px;width:36px;height:36px;border-radius:50%}
.value .go::after{content:"→";color:#fff;font-size:18px;display:flex;justify-content:center;line-height:34px}
.about-text{left:735px;top:2060px;width:355px}
.about-text h2{font-size:38px;font-weight:300;color:var(--black);margin-bottom:18px}
.about-text p{font-size:15px;line-height:28px;color:#222;margin-bottom:26px}
.tabs{top:2983px;left:188px;display:flex;gap:30px}
.tab{height:55px;padding:0 18px;display:flex;align-items:center;font-size:15px;font-weight:700;text-transform:uppercase;white-space:nowrap}
.tab.on{background:var(--pink);color:#fff}
.tab.off{background:var(--pink-soft);color:#222}
.features{left:112px;top:3085px;width:580px;font-size:18px;line-height:40px;color:#222}
.features li{list-style:none;display:flex;align-items:center;gap:12px;white-space:nowrap}
.testi-band{left:0;top:3566px;width:1200px;height:600px;background:linear-gradient(180deg,var(--pink-wash),#fff 80%)}
.testi{top:3840px;width:302px;height:143px;background:#fff;box-shadow:0 4px 18px rgba(0,0,0,.06);text-align:center;padding-top:38px}
.testi h4{font-size:17px;font-weight:700;color:var(--black)}
.stars{color:#F2B200;font-size:10px;letter-spacing:2px;margin:3px 0}
.testi p{font-size:12.5px;line-height:22px;color:#555;padding:0 18px}
.avatar{top:3770px;width:72px;height:72px;border-radius:50%;background:linear-gradient(135deg,#d9d9d9,#a8a8a8);border:4px solid #fff}
.footer{left:0;top:4290px;width:1200px;height:372px;background:var(--black);color:#fff}
.footer h5{font-size:19px;font-weight:700;text-transform:uppercase;margin-bottom:18px}
.footer ul{list-style:none;font-size:14px;line-height:35px;color:#ddd}
.footer ul li::before{content:"›";color:var(--grey);margin-right:8px}
.social{width:28px;height:28px;border-radius:50%;border:1.5px solid #fff}
.contact-row{display:flex;gap:16px;align-items:flex-start;font-size:14px;line-height:26px;color:#ddd;margin-bottom:18px;white-space:nowrap}
.contact-row .ci{width:32px;height:32px;border-radius:50%;background:#fff;flex:none;display:flex;align-items:center;justify-content:center}
</style>
</head>
<body>

<!-- HERO -->
<svg class="abs" style="left:0;top:0" width="1200" height="730" viewBox="0 0 1200 730">
  <defs>
    <linearGradient id="heroPhoto" x1="0" y1="0" x2="1" y2="0">
      <stop offset="0" stop-color="#f4f4f4"/><stop offset=".5" stop-color="#e9e7e4"/><stop offset=".7" stop-color="#c58a4c"/><stop offset="1" stop-color="#dcdfe2"/>
    </linearGradient>
  </defs>
  <polygon points="0,0 1200,0 1200,440 272,670 0,490" fill="url(#heroPhoto)" role="img" aria-label="Photo of a smiling young professional working on a laptop in a bright office"/>
  <polygon points="40,543 272,720 896,561 272,690" fill="var(--pink)"/>
</svg>
<div class="abs brand" style="left:80px;top:30px">BLOOM The Answer<span class="dot"></span></div>
<nav class="abs nav"><span class="active">HOME</span><span>ABOUT US</span><span>SERVICES</span><span>BLOG</span><span>SOLUTION</span><span class="btn">Get a quote</span><span>EN</span></nav>
<h1 class="abs hero-title">Your partner in<br>smarter payrolling</h1>
<p class="abs hero-text">We take care of contracts, administration, and compliance—so you can focus on your career. Flexible, transparent, and compliant solutions—designed to support professionals and companies alike.</p>
<span class="abs btn hero-btn">Discover payrolling</span>

<!-- SERVICES -->
<h2 class="abs section-title" style="top:780px">Discover all <b>our services</b></h2>
<div class="abs rule" style="top:852px"></div>
<div class="abs service" style="left:108px;top:912px"><div class="ic"></div><h3>Payrolling</h3><p>Ut enim ad minim veniam, quis nostrud exercitation ullamco laboris nisi ut aliquip ex ea commodo consequat.</p></div>
<div class="abs service" style="left:450px;top:912px"><div class="ic"></div><h3>Sourcing</h3><p>Ut enim ad minim veniam, quis nostrud exercitation ullamco laboris nisi ut aliquip ex ea commodo consequat.</p></div>
<div class="abs service" style="left:775px;top:912px"><div class="ic"></div><h3>Payroll Outsourcing</h3><p>Ut enim ad minim veniam, quis nostrud exercitation ullamco laboris nisi ut aliquip ex ea commodo consequat.</p></div>

<!-- VALUES -->
<h2 class="abs section-title" style="top:1212px">Working with BLOOM payroll means<br><b>working with a partner</b></h2>
<div class="abs rule" style="top:1342px"></div>
<div class="abs value" style="left:72px"><div class="shape"></div><div class="inner">
  <svg width="60" height="60" viewBox="0 0 60 60" fill="none" stroke="#222" stroke-width="2"><rect x="14" y="18" width="30" height="30"/><circle cx="40" cy="14" r="8" stroke="var(--pink)"/><path d="M20 40l7-8 6 5 8-10"/></svg>
  <h3>Market leader</h3><p>Duis aute irure dolor in reprehenderit in voluptate velit esse cillum dolore eu eprehe nderit in volupta tef pariatur.</p></div>
  <span class="go" style="background:var(--black)"></span></div>
<div class="abs value" style="left:322px"><div class="shape"></div><div class="inner">
  <svg width="60" height="60" viewBox="0 0 60 60" fill="none" stroke="#222" stroke-width="2"><rect x="12" y="12" width="28" height="38"/><path d="M18 22h16M18 30h16M18 38h10"/><path d="M40 8l10 4v10c0 6-5 10-10 12-5-2-10-6-10-12V12z" stroke="var(--pink)"/></svg>
  <h3>Compliant</h3><p>Duis aute irure dolor in reprehenderit in voluptate velit esse cillum dolore eu eprehe nderit in volupta tef pariatur.</p></div>
  <span class="go" style="background:var(--pink)"></span></div>
<div class="abs value" style="left:570px"><div class="shape"></div><div class="inner">
  <svg width="60" height="60" viewBox="0 0 60 60" fill="none" stroke="#222" stroke-width="2"><rect x="10" y="18" width="40" height="26"/><path d="M6 48h48"/><circle cx="30" cy="31" r="6" stroke="var(--pink)"/></svg>
  <h3>Agile and responsive</h3><p>Duis aute irure dolor in reprehenderit in voluptate velit esse cillum dolore eu eprehe nderit in volupta tef pariatur.</p></div>
  <span class="go" style="background:var(--black)"></span></div>
<div class="abs value" style="left:824px"><div class="shape"></div><div class="inner">
  <svg width="60" height="60" viewBox="0 0 60 60" fill="none" stroke="#222" stroke-width="2"><circle cx="30" cy="22" r="7" stroke="var(--pink)"/><rect x="20" y="36" width="20" height="14"/><path d="M30 29v7M12 14h8M40 14h8M14 44h6M40 44h6"/></svg>
  <h3>100% digital</h3><p>Duis aute irure dolor in reprehenderit in voluptate velit esse cillum dolore eu eprehe nderit in volupta tef pariatur.</p></div>
  <span class="go" style="background:var(--pink)"></span></div>

<!-- ABOUT -->
<svg class="abs" style="left:0;top:1860px" width="1200" height="935" viewBox="0 0 1200 935">
  <defs>
    <linearGradient id="aboutPhoto" x1="0" y1="0" x2="1" y2="1">
      <stop offset="0" stop-color="#c9a27a"/><stop offset=".4" stop-color="#e6e2dc"/><stop offset="1" stop-color="#f3f3f3"/>
    </linearGradient>
  </defs>
  <polygon points="0,230 310,162 935,130 1160,195 1200,210 1200,700 0,700" fill="#f6f6f6"/>
  <polygon points="0,230 310,162 690,150 690,760 265,850 0,700" fill="url(#aboutPhoto)" role="img" aria-label="Photo of a cheerful businesswoman celebrating at a laptop with colleagues in an office"/>
  <polygon points="308,162 932,8 1160,195 930,50" fill="var(--pink)"/>
  <polygon points="0,700 265,922 895,762 265,880" fill="var(--pink)"/>
</svg>
<div class="abs about-text">
  <h2>ABOUT&nbsp; BLOOM</h2>
  <p>At BLOOM The Answer, we make payrolling simple, transparent, and efficient. As specialists in employment outsourcing, we handle all administrative, legal, and contractual aspects—so you can focus on what matters most: your work and your clients.</p>
  <p>Backed by our mother company BLOOM The Horizon and in synergy with our sister company BLOOM Your Stride, we bring proven expertise and a people-first approach.</p>
  <span class="btn">Read more</span>
</div>

<!-- TOOLS -->
<h2 class="abs section-title" style="top:2806px">High-performance and<br><b>secure digital tools</b></h2>
<div class="abs tabs"><span class="tab on">Consultant space | Managing your activities</span><span class="tab off">Business space | Service management</span></div>
<div class="abs features">
  <p>This cross-platform solution immediately provides you<br>with the following features:</p>
  <ul>
    <li><svg width="24" height="16" viewBox="0 0 24 16" fill="none" stroke="var(--pink)" stroke-width="2.5"><path d="M2 8l5 5 9-11M10 13l11-11"/></svg>Enter your activity report</li>
    <li><svg width="24" height="16" viewBox="0 0 24 16" fill="none" stroke="var(--pink)" stroke-width="2.5"><path d="M2 8l5 5 9-11M10 13l11-11"/></svg>Have the status of your invoices in real time</li>
    <li><svg width="24" height="16" viewBox="0 0 24 16" fill="none" stroke="var(--pink)" stroke-width="2.5"><path d="M2 8l5 5 9-11M10 13l11-11"/></svg>Have dematerialized pay slips</li>
    <li><svg width="24" height="16" viewBox="0 0 24 16" fill="none" stroke="var(--pink)" stroke-width="2.5"><path d="M2 8l5 5 9-11M10 13l11-11"/></svg>Find all your documents and sign them directly online</li>
    <li><svg width="24" height="16" viewBox="0 0 24 16" fill="none" stroke="var(--pink)" stroke-width="2.5"><path d="M2 8l5 5 9-11M10 13l11-11"/></svg>Obtain the contact details of your Human Resources advisor</li>
  </ul>
  <p>and your account manager</p>
</div>
<span class="abs btn" style="left:112px;top:3418px;padding:17px 26px">View more</span>
<div class="abs" role="img" aria-label="Laptop displaying a payroll report dashboard with charts" style="left:672px;top:3100px;width:456px;height:330px;background:linear-gradient(160deg,#2a4a8a,#5fa0d8 55%,#c9ced4);border-radius:10px 10px 4px 4px"></div>

<!-- TESTIMONIALS -->
<div class="abs testi-band"></div>
<h2 class="abs section-title" style="top:3632px">What our <b>customer says</b></h2>
<div class="abs rule" style="top:3700px"></div>
<div class="abs testi" style="left:112px"><h4>Marc Dellinger</h4><div class="stars">★★★★★</div><p>Temporibus autem quibusdam et aut officiis debitis aut rerum necessitatibus saepe eveniet ut et voluptates</p></div>
<div class="abs testi" style="left:451px"><h4>Laurent Vassey</h4><div class="stars">★★★★★</div><p>Itaque earum rerum hic tenetur a sapiente delectus, reiciendis voluptatibus maiores alias consequatur aut</p></div>
<div class="abs testi" style="left:790px"><h4>Clara Winsor</h4><div class="stars">★★★★★</div><p>Nam libero tempore, cum soluta nobis est eligendi optio cumque nihil impedit quo minus id quod</p></div>
<div class="abs avatar" role="img" aria-label="Portrait of client" style="left:227px"></div>
<div class="abs avatar" role="img" aria-label="Portrait of client" style="left:566px"></div>
<div class="abs avatar" role="img" aria-label="Portrait of client" style="left:905px"></div>

<!-- FOOTER -->
<svg class="abs" style="left:0;top:4060px" width="1200" height="240" viewBox="0 0 1200 240">
  <polygon points="0,150 300,175 935,10 1200,170 1200,240 0,240" fill="var(--black)"/>
  <polygon points="300,175 935,10 1160,200 935,45" fill="var(--pink)"/>
</svg>
<footer class="abs footer">
  <div class="abs brand" style="left:112px;top:62px;color:#fff;font-size:30px">BLOOM The Answer</div>
  <div class="abs" style="left:112px;top:185px;display:flex;gap:17px">
    <span class="social" style="background:var(--pink);border-color:var(--pink)"></span><span class="social"></span><span class="social"></span><span class="social"></span>
  </div>
  <div class="abs" style="left:481px;top:45px"><h5>Quick link</h5><ul><li>Home</li><li>About</li><li>Services</li><li>Testimonials</li><li>Contact Us</li></ul></div>
  <div class="abs" style="left:715px;top:45px"><h5>Help links</h5><ul><li>FAQ</li><li>Terms of use</li><li>Privacy Policy</li><li>Support Links</li><li>Conditions</li></ul></div>
  <div class="abs" style="left:914px;top:45px"><h5>Contact us</h5>
    <div class="contact-row"><span class="ci"><svg width="14" height="18" viewBox="0 0 14 18"><path d="M7 0a7 7 0 0 0-7 7c0 5 7 11 7 11s7-6 7-11a7 7 0 0 0-7-7z" fill="#000"/><circle cx="7" cy="7" r="2.5" fill="#fff"/></svg></span><span>Bloom<br>United States</span></div>
    <div class="contact-row"><span class="ci"><svg width="16" height="16" viewBox="0 0 16 16"><path d="M3 1l3 3-2 2c1 2 3 4 5 5l2-2 3 3-2 3C7 15 1 9 1 3z" fill="#000"/></svg></span><span style="line-height:32px">+1 555 014 2290</span></div>
    <div class="contact-row"><span class="ci"><svg width="16" height="12" viewBox="0 0 16 12"><rect width="16" height="12" fill="#000"/><path d="M0 0l8 6 8-6" stroke="#fff" fill="none"/></svg></span><span style="line-height:32px">info@bloom-answer.com</span></div>
  </div>
  <div class="abs" style="left:112px;top:300px;width:976px;height:1px;background:#444"></div>
  <p class="abs" style="left:0;width:1200px;top:322px;text-align:center;font-size:14px;color:#ddd">Copyrights@2025.Bloom.All Rights Reserved</p>
</footer>

</body>
</html>
```